Steady Crews: Keeping Staff from Drifting Away
Everyday People Guides for the Shopkeeper and Reluctant Personnel Lead
Steady Crews: Keeping Staff from Drifting Away - Books
Creative Brief
title: Everyday People Guides for the Shopkeeper and Reluctant Personnel Lead E-book covers: I'd also like two high-resolution JPG cover images (one front and one back), sized at 5.5" x 8.5" with all elements stopping within .5" of the page edge. A low-resolution version of each image must also be supplied for use in e-book format. These images will include: Front cover: • Image An eye-catching photo/illustration representing the topic of the book (managing costly employee turnover) • Book title Steady Crews: Keeping Staff from Drifting Away • Subtitle with icon Everyday People Guides for the Shopkeeper and Reluctant Personnel Lead, Book 1 • Tagline none • Author name Rosalind Pettigrew, SPHR Back cover: • Image Mugshot of author • Publisher name RTKV Publishing • Author blurb & image (may be inside book) • Barcode Leave space in lower right-hand corner for Bookvane to insert. • Book blurb If you're a small-business owner or entrepreneur thinking, "How in the world do I stop this organization's crazy turnover?" this e-book is for you. Steady Crews: Keeping Staff from Drifting Away by certified Human Resources consultant Rosalind Pettigrew provides simple tools for those thrown into the role of "accidental HR manager." Compiled as book one in Pettigrew's series, Everyday People Guides for the Shopkeeper and Reluctant Personnel Lead, it delivers quick access to critical, yet simple, techniques and processes to help you manage HR issues like recruitment/hiring, performance, and more. Filled with explanations and advice, worksheets and handy calculators, you'll find a solid foundation of information to help you manage your organization's HR issues... without the learning curve.
Books
Corporate executives in small businesses and entrepreneurs tasked with the role of managing Human Resources unexpectedly.
Book one cover art: • Book series icon • 2 high-resolution JPG files (1 front cover, 1 back cover) • 5.5" x 8.5" final size, with a .5" margin at all page edges • 2 low-res JPG files of the same front- and back-cover art for use in e-book format • Book title must be large enough to read in thumbnail size (like book thumbnails viewed on Bookvane) • Designer will need to procure: o Author mug shot (if not inside book) o Final book blurb for back cover o Book formatting specs from PrintHollow.com

```html
<!DOCTYPE html>
<html lang="en">
<head>
<meta charset="utf-8">
<title>Steady Crews: Keeping Staff from Drifting Away — Cover Spread</title>
<link rel="stylesheet" href="https://fonts.googleapis.com/css2?family=Arimo:ital,wght@0,400;0,700;1,400;1,700&display=swap">
<style>
  :root {
    --page-bg: #ffffff;
    --back-light: #f4f4f4;
    --back-mid: #c9c9c9;
    --back-dark: #7e7e7e;
    --spine-top: #6f6f6f;
    --spine-body: #a3a3a3;
    --pattern-dark: #566f65;
    --pattern-mid: #8fa79c;
    --pattern-light: #d7e1da;
    --band-light: rgba(255, 255, 255, 0.92);
    --ink: #1f2a26;
    --ink-soft: #3a3a3a;
    --white: #ffffff;
  }
  * { box-sizing: border-box; margin: 0; padding: 0; }
  html, body {
    width: 1200px; height: 670px; overflow: hidden;
    background: var(--page-bg);
    font-family: "Arimo", Arial, sans-serif;
  }
  .cover-spread {
    position: absolute; left: 195px; top: 35px;
    width: 809px; height: 600px;
    box-shadow: 0 0 0 1px #bdbdbd;
  }
  .back-cover {
    position: absolute; left: 0; top: 0; width: 386px; height: 600px;
    background:
      radial-gradient(ellipse 70% 55% at 52% 58%, var(--back-light) 0%, var(--back-mid) 55%, var(--back-dark) 100%);
  }
  .back-blurb {
    position: absolute; left: 16px; top: 253px; width: 331px; height: 172px;
    background: rgba(255, 255, 255, 0.85);
    border-radius: 4px;
    padding: 12px 14px;
    font-size: 8.6px; line-height: 1.35; color: var(--ink-soft);
  }
  .back-blurb p + p { margin-top: 7px; }
  .publisher {
    position: absolute; left: 18px; bottom: 26px;
    font-size: 16px; color: var(--ink-soft);
  }
  .spine {
    position: absolute; left: 386px; top: 0; width: 52px; height: 600px;
    background: linear-gradient(to bottom, var(--spine-top) 0 150px, var(--spine-body) 150px 100%);
    border-left: 1px solid #8a8a8a; border-right: 1px solid #8a8a8a;
  }
  .spine-author, .spine-title {
    position: absolute; left: 50%; transform: translateX(-50%);
    writing-mode: vertical-rl; white-space: nowrap;
  }
  .spine-author { top: 18px; font-size: 13px; color: var(--white); }
  .spine-title { top: 200px; font-size: 14px; font-style: italic; color: var(--ink); }
  .front-cover {
    position: absolute; left: 438px; top: 0; width: 371px; height: 600px;
    overflow: hidden;
  }
  .front-pattern {
    position: absolute; inset: 0;
    background:
      radial-gradient(circle at 25% 20%, var(--pattern-light) 0%, transparent 35%),
      radial-gradient(circle at 80% 80%, var(--pattern-light) 0%, transparent 30%),
      linear-gradient(160deg, var(--pattern-mid), var(--pattern-dark) 60%, var(--pattern-mid));
  }
  .title-band {
    position: absolute; left: 0; right: 0; top: 150px; height: 220px;
    background: radial-gradient(ellipse 75% 55% at 50% 50%, var(--band-light) 0%, rgba(255,255,255,0.55) 60%, rgba(255,255,255,0) 100%);
  }
  .author {
    position: absolute; left: 68px; top: 172px;
    font-size: 15px; color: var(--ink);
  }
  .book-title {
    position: absolute; left: 28px; right: 20px; top: 208px;
    font-size: 25px; font-weight: 700; line-height: 1.15; color: var(--ink);
    text-align: center;
  }
  .subtitle {
    position: absolute; left: 40px; right: 18px; top: 284px;
    font-size: 12px; font-weight: 700; font-style: italic; line-height: 1.3; color: var(--ink);
    text-align: center;
  }
  .series-number { display: block; text-align: right; }
</style>
</head>
<body>
  <main class="cover-spread">
    <section class="back-cover">
      <div class="back-blurb">
        <p>If you're a small-business owner or entrepreneur thinking, "How in the world do I stop this organization's crazy turnover?" this e-book is for you. Steady Crews: Keeping Staff from Drifting Away by certified Human Resources consultant Rosalind Pettigrew provides simple tools for those thrown into the role of "accidental HR manager."</p>
        <p>Compiled as book one in Pettigrew's series, Everyday People Guides for the Shopkeeper and Reluctant Personnel Lead, it delivers quick access to critical, yet simple, techniques and processes to help you manage HR issues like recruitment/hiring, performance, and more. Filled with explanations and advice, worksheets and handy calculators, you'll find a solid foundation of information to help you manage your organization's HR issues... without the learning curve.</p>
      </div>
      <p class="publisher">RTKV Publishing</p>
    </section>

    <section class="spine">
      <p class="spine-author">Rosalind Pettigrew, SPHR</p>
      <p class="spine-title">Steady Crews: Keeping Staff from Drifting Away</p>
    </section>

    <section class="front-cover">
      <div class="front-pattern" role="img" aria-label="Swirling grey-green damask pattern filling the front cover"></div>
      <div class="title-band"></div>
      <p class="author">Rosalind Pettigrew, SPHR</p>
      <h1 class="book-title">Steady Crews: Keeping Staff from Drifting Away</h1>
      <p class="subtitle">Everyday People Guides for the Shopkeeper and Reluctant Personnel Lead <span class="series-number">Book 1</span></p>
    </section>
  </main>
</body>
</html>
```